Business Card Design Project

Name Martin Holroyd
Company Veldmark Site Restoration Crew
address 22/7 Penbrook street
Wattle Downs
Brisbane Queensland
Australia 4110,
0498357261

Things that we do Mould inspection and Remediation,
Crime and Trauma Scene Cleanup and Decontamination
Drug lab Decontamination and needle cleanups.
Odor control
Air quality Testing and swabs,
latest equipment
Hydroxyl machines, ozone machines ,Sterilising lights ,Comercial Steam machines ,
Thermal imaging, Bacteria testing equipment
Fully trained personel

Reason: One day is not enough time to get designs i dont why the Current deadline is only one day

I do not need purovex in the cards, that was only a sample, The Business name isĀ 

Veldmark Site Restoration Crew.

Target Market(s)

Government agencies ,Police and real-estates, housing companies, Coroners

Industry/Entity Type

Business

Requirements
Must have
• Must tell what we are about
Nice to have
• raised letters or good background

```html
<!DOCTYPE html>
<html lang="en">
<head>
<meta charset="utf-8">
<title>Veldmark Site Restoration Crew – Business Card</title>
<link rel="stylesheet" href="https://fonts.googleapis.com/css2?family=Cousine&family=Arimo:wght@400;700&family=Tinos:wght@700&display=swap">
<style>
  :root {
    --page: #ffffff;
    --card: #333333;
    --card-edge: #1e1e1e;
    --band: #6d6e70;
    --ink-light: #ffffff;
    --ink-dark: #2a2a2a;
    --accent-red: #d9312b;
    --print-grey: #9a9a9a;
    --tape-yellow: #f2d21b;
    --sign-yellow: #f7c81e;
  }
  * { margin: 0; padding: 0; box-sizing: border-box; }
  html, body {
    width: 1200px; height: 381px; overflow: hidden;
    background: var(--page);
  }
  .sheet { position: relative; width: 1200px; height: 381px; }

  .card {
    position: absolute; top: 8px; height: 363px;
    background: var(--card);
    border: 1px solid var(--card-edge);
    overflow: hidden;
  }
  .card--front { left: 8px; width: 682px; }
  .card--back { left: 706px; width: 486px; }

  .brand-band {
    position: absolute; left: 0; top: 0; bottom: 0;
    background: var(--band);
  }
  .card--front .brand-band { width: 132px; }
  .card--back .brand-band { width: 92px; }

  .brand {
    position: absolute; left: 0; right: 0;
    display: flex; flex-direction: column; align-items: center; gap: 10px;
  }
  .card--front .brand { top: 22px; }
  .card--back .brand { top: 30px; }
  .brand-mark { width: 40px; height: 40px; background: var(--accent-red); }
  .card--back .brand-mark { width: 30px; height: 30px; }
  .brand-name {
    font-family: "Tinos", serif; font-weight: 700;
    color: var(--ink-dark); font-size: 19px; letter-spacing: 0.5px;
  }
  .card--back .brand-name { font-size: 14px; letter-spacing: 0.3px; }

  .crime-scene-art {
    position: absolute; left: 265px; top: 0; width: 400px; height: 363px;
    background:
      radial-gradient(ellipse 45% 40% at 50% 55%, #cfcfcf 0%, var(--print-grey) 55%, rgba(154,154,154,0) 100%),
      linear-gradient(150deg, rgba(242,210,27,0) 40%, rgba(242,210,27,0.35) 60%, rgba(242,210,27,0) 80%);
  }

  .contact {
    position: absolute; left: 18px; top: 180px;
    font-family: "Cousine", monospace; font-size: 20px; line-height: 25px;
    color: var(--ink-light); white-space: nowrap;
  }

  .services, .equipment {
    position: absolute; top: 40px;
    font-family: "Arimo", sans-serif; color: var(--ink-light);
    font-size: 15px; line-height: 19px; white-space: nowrap;
  }
  .services { left: 101px; }
  .equipment { left: 311px; z-index: 2; }
  .section-title {
    color: var(--accent-red); font-weight: 700; font-size: 15px;
  }
  .service-list { list-style: none; }
  .service-list li { position: relative; padding-left: 23px; }
  .service-list li::before {
    content: ""; position: absolute; left: 4px; top: 8px;
    width: 4px; height: 4px; border-radius: 50%; background: var(--ink-light);
  }

  .hazard-sign-art {
    position: absolute; left: 375px; top: 58px; width: 111px; height: 262px;
    background: radial-gradient(ellipse 60% 55% at 55% 50%, #fff3b0 0%, var(--sign-yellow) 60%, #c99a12 100%);
    clip-path: polygon(40% 0, 100% 0, 100% 100%, 0 88%, 0 55%);
  }
</style>
</head>
<body>
<main class="sheet">

  <section class="card card--front">
    <div class="brand-band">
      <div class="brand">
        <span class="brand-mark"></span>
        <span class="brand-name">VELDMARK</span>
      </div>
    </div>
    <div class="crime-scene-art" role="img" aria-label="Illustration of a fingerprint crossed by yellow crime scene tape"></div>
    <div class="contact">
      Name: Martin Holroyd<br>
      Company: Veldmark Site<br>
      Restoration Crew<br>
      Address: 22/7 Penbrook street<br>
      Wattle Downs Brisbane Queensland<br>
      Australia 4110,<br>
      Phone: 0498357261
    </div>
  </section>

  <section class="card card--back">
    <div class="brand-band">
      <div class="brand">
        <span class="brand-mark"></span>
        <span class="brand-name">VELDMARK</span>
      </div>
    </div>
    <div class="services">
      <h2 class="section-title">Things that we do :</h2>
      <ul class="service-list">
        <li>Mould inspection<br>and Remediation</li>
        <li>Crime and Trauma<br>Scene Cleanup<br>and<br>Decontamination</li>
        <li>Decontamination</li>
        <li>Drug lab<br>Decontamination<br>and needle<br>cleanups.</li>
        <li>Odor control</li>
        <li>Air quality Testing<br>and swabs</li>
      </ul>
    </div>
    <div class="hazard-sign-art" role="img" aria-label="Illustration of a yellow biohazard warning sign"></div>
    <div class="equipment">
      <h2 class="section-title">Latest Equipment:</h2>
      <p>Hydroxyl machines,<br>ozone machines<br>,Sterilising lights<br>,Comercial Steam<br>machines ,<br>Thermal imaging,<br>Bacteria testing<br>equipment<br>Fully trained personel</p>
    </div>
  </section>

</main>
</body>
</html>
```